International Wine events organiser seeks simple but stunning business card

I am a freelance events, marketing and PR provider specialised in the Wine industry. I help wineries and wine regions reach trade and consumers in foreign markets through events, help with the websites and communications, press trips and promotional activities. I am looking for a business card which is simple yet effective and is linked to events and communication.

I work mainly - but exclusively - with Italian wineries organising events for them in foreign market.s

I would like to use red in the logo as my present website (lenamorvick.com) used grey and red (although I will be changing the design at a later date).

Target Market(s)

Wine producers, promotional bodies in wine sector, companies looking to hire event organisers,

Industry/Entity Type

Marketing

Requirements
Must have
• My Name - Lena Morvick
My address
My phone
My website : www.lenamorvick.com
my Blog : velvetandtone.me

Should not have
• Butterflies, stars, flowers, anything not particularly linked to wine - would like to keep it simple, modern and eye-catching without being too cliche.

```html
<!DOCTYPE html>
<html lang="en">
<head>
<meta charset="utf-8">
<title>Lena Morvick – Business Card</title>
<link rel="stylesheet" href="https://fonts.googleapis.com/css2?family=Jost:wght@400&display=swap">
<style>
  :root {
    --backdrop: #adadad;
    --card-white: #ffffff;
    --wine-red: #a8171a;
    --name-maroon: #5b2a2f;
    --tagline-mauve: #8b5d62;
    --illustration-red: #a3191c;
    --illustration-pink: #f3b6b8;
    --card-shadow: rgba(70, 62, 110, 0.75);
    --text-light: #ffffff;
  }
  html, body {
    margin: 0;
    padding: 0;
    width: 997px;
    height: 1200px;
    overflow: hidden;
    background: var(--backdrop);
    font-family: "Jost", "Futura", sans-serif;
  }
  .canvas {
    position: relative;
    width: 997px;
    height: 1200px;
  }
  .card {
    position: absolute;
    box-shadow: 9px 9px 6px var(--card-shadow);
  }
  .card--front {
    left: 140px;
    top: 118px;
    width: 730px;
    height: 437px;
    background: var(--card-white);
  }
  .card--back {
    left: 146px;
    top: 658px;
    width: 734px;
    height: 440px;
    background: var(--wine-red);
  }
  .illustration {
    position: absolute;
    display: block;
  }
  .card--front .illustration {
    left: 31px;
    top: 45px;
  }
  .card--back .illustration {
    left: 492px;
    top: 40px;
  }
  .brand-name {
    position: absolute;
    left: 207px;
    top: 242px;
    margin: 0;
    font-weight: 400;
    font-size: 62px;
    line-height: 1;
    letter-spacing: 3px;
    color: var(--name-maroon);
    white-space: nowrap;
  }
  .tagline {
    position: absolute;
    left: 208px;
    top: 305px;
    margin: 0;
    font-size: 30px;
    line-height: 38px;
    letter-spacing: 0.3px;
    color: var(--tagline-mauve);
    white-space: nowrap;
  }
  .contact {
    position: absolute;
    left: 56px;
    top: 54px;
    margin: 0;
    font-size: 27px;
    line-height: 38px;
    letter-spacing: 0.5px;
    color: var(--text-light);
    font-style: normal;
  }
  .contact p {
    margin: 0 0 38px;
  }
  .contact p:last-child {
    margin: 0;
  }
</style>
</head>
<body>
<main class="canvas">

  <section class="card card--front" aria-label="Business card front">
    <svg class="illustration" width="160" height="329" viewBox="0 0 160 329" role="img" aria-label="Hand-drawn sketch of a wine bottle and wine glass">
      <rect width="160" height="329" fill="var(--illustration-red)" opacity="0.85"/>
    </svg>
    <h1 class="brand-name">LENA MORVICK</h1>
    <p class="tagline">Communication and Events<br>for the World of Wine</p>
  </section>

  <section class="card card--back" aria-label="Business card back">
    <address class="contact">
      <p>Lena Morvick<br>Lindenhofer Strasse, 48<br>81547 Munich</p>
      <p>lena@lenamorvick.com<br>Tel: +49 170 5820 317<br>www.lenamorvick.com<br>velvetandtone.me</p>
    </address>
    <svg class="illustration" width="168" height="328" viewBox="0 0 168 328" role="img" aria-label="Hand-drawn sketch of a wine bottle and wine glass">
      <rect width="168" height="328" fill="var(--illustration-pink)" opacity="0.85"/>
    </svg>
  </section>

</main>
</body>
</html>
```